Business Cards Design Needed

We require a design for the front side (contact details side) for a business card.

The details/fields required are below with example data:

1. Name: Mark Tolbert
2. Title: CEO
3. Email: mark@[login to view URL]
4. Phone number: +64 27 908 3152
5. Website address: [login to view URL]

Logo & icon assets are attached for your use where you see applicable on the business cards.

Please do not worry about the reverse side design but so you are aware for front side design purposes, the reverse side will be full colour gradient (using logo colours) with white logo in the centre of the card.

```html
<!DOCTYPE html>
<html lang="en">
<head>
<meta charset="utf-8">
<title>Vellora Business Card</title>
<link href="https://fonts.googleapis.com/css2?family=Montserrat:wght@300;400;500;600&display=swap" rel="stylesheet">
<style>
  :root {
    --teal: #3cc8bf;
    --teal-deep: #25b0a7;
    --teal-light: #8fe6df;
    --ink: #1f2a2c;
    --paper: #ffffff;
    --stage: #eef1f1;
  }
  * { box-sizing: border-box; margin: 0; padding: 0; }
  html, body {
    width: 1200px; height: 1200px; overflow: hidden;
    background: var(--stage);
    font-family: "Montserrat", sans-serif;
  }
  .stage {
    position: relative; width: 1200px; height: 1200px;
  }
  .card {
    position: absolute; left: 180px; width: 840px; height: 480px;
    background: var(--paper);
    overflow: hidden;
    box-shadow: 0 6px 24px rgba(0,0,0,0.12);
  }
  .card--reverse { top: 90px; }
  .card--front { top: 630px; }

  /* reverse side */
  .band { position: absolute; left: 0; right: 0; }
  .band--top {
    top: 0; height: 30px;
    background: linear-gradient(90deg, var(--teal-light), var(--teal) 40%, var(--teal-deep));
  }
  .band--bottom {
    bottom: 0; height: 30px;
    background: linear-gradient(90deg, var(--teal-deep), var(--teal) 60%, var(--teal-light));
  }
  .rule { position: absolute; left: 0; right: 0; height: 2px; background: var(--teal); }

  .brand {
    position: absolute; display: flex; align-items: center; gap: 14px;
    color: var(--teal); font-weight: 500; letter-spacing: 1px;
  }
  .brand__dot { border-radius: 50%; background: var(--teal); }
  .card--reverse .brand {
    left: 50%; top: 50%; transform: translate(-50%, -50%); font-size: 52px;
  }
  .card--reverse .brand__dot { width: 30px; height: 30px; }

  /* front side */
  .front-band--top {
    top: 0; height: 26px;
    background: linear-gradient(90deg, var(--teal-light), var(--teal) 50%, var(--teal-deep));
  }
  .front-band--bottom {
    bottom: 0; height: 64px;
    background: linear-gradient(90deg, var(--teal), var(--teal-light) 50%, var(--teal));
  }
  .identity { position: absolute; left: 62px; top: 66px; width: 300px; }
  .identity__name { font-size: 34px; line-height: 1.1; white-space: nowrap; }
  .identity__first { color: var(--teal); font-weight: 300; }
  .identity__last { color: var(--ink); font-weight: 500; }
  .identity__title {
    color: var(--teal); font-size: 26px; font-weight: 400;
    text-align: right; padding-right: 40px; margin-top: 2px;
  }
  .identity__rule {
    margin-top: 12px; margin-left: 20px; width: 260px; height: 2px;
    background: linear-gradient(90deg, transparent, var(--teal) 40%, transparent);
  }
  .contacts {
    position: absolute; left: 62px; top: 196px; list-style: none;
    font-size: 17px; color: var(--ink);
  }
  .contacts li { display: flex; align-items: center; gap: 14px; height: 34px; }
  .contacts svg { width: 18px; height: 18px; fill: none; stroke: var(--teal-deep); stroke-width: 2; }
  .divider { position: absolute; left: 360px; top: 150px; }
  .card--front .brand { left: 540px; top: 200px; font-size: 46px; }
  .card--front .brand__dot { width: 26px; height: 26px; }
</style>
</head>
<body>
<main class="stage">

  <section class="card card--reverse" aria-label="Card reverse side">
    <div class="band band--top"></div>
    <div class="rule" style="top:44px"></div>
    <div class="rule" style="top:56px"></div>
    <div class="rule" style="top:68px"></div>

    <div class="brand">
      <span class="brand__dot"></span>
      <span class="brand__name">Vellora</span>
    </div>

    <div class="rule" style="bottom:68px"></div>
    <div class="rule" style="bottom:56px"></div>
    <div class="rule" style="bottom:44px"></div>
    <div class="band band--bottom"></div>
  </section>

  <section class="card card--front" aria-label="Card contact side">
    <div class="band front-band--top"></div>

    <div class="identity">
      <h1 class="identity__name">
        <span class="identity__first">Mark</span>
        <span class="identity__last">Tolbert</span>
      </h1>
      <p class="identity__title">CEO</p>
      <div class="identity__rule"></div>
    </div>

    <ul class="contacts">
      <li>
        <svg viewBox="0 0 24 24"><path d="M5 3h4l2 5-3 2a12 12 0 0 0 6 6l2-3 5 2v4a2 2 0 0 1-2 2A18 18 0 0 1 3 5a2 2 0 0 1 2-2z"/></svg>
        <span>+64 27 908 3152</span>
      </li>
      <li>
        <svg viewBox="0 0 24 24"><rect x="3" y="5" width="18" height="14" rx="2"/><path d="M3 7l9 6 9-6"/></svg>
        <span>mark@[login to view URL]</span>
      </li>
      <li>
        <svg viewBox="0 0 24 24"><circle cx="12" cy="12" r="9"/><path d="M3 12h18M12 3c3 3 3 15 0 18M12 3c-3 3-3 15 0 18"/></svg>
        <span>Vellora.co.nz</span>
      </li>
    </ul>

    <svg class="divider" width="80" height="200" viewBox="0 0 80 200">
      <defs>
        <linearGradient id="divider-fade" x1="0" y1="0" x2="0" y2="1">
          <stop offset="0" stop-color="#3cc8bf" stop-opacity="0"/>
          <stop offset="0.5" stop-color="#3cc8bf"/>
          <stop offset="1" stop-color="#3cc8bf" stop-opacity="0"/>
        </linearGradient>
      </defs>
      <line x1="72" y1="0" x2="8" y2="200" stroke="url(#divider-fade)" stroke-width="3"/>
    </svg>

    <div class="brand">
      <span class="brand__dot"></span>
      <span class="brand__name">Vellora</span>
    </div>

    <div class="band front-band--bottom"></div>
  </section>

</main>
</body>
</html>
```